Vehicle Wrap (Van) - HVAC Company

We need a vehicle wrap for our work van. The van is a Harvick Trellan cargo liner 2700 2019 standard, and we would like to have a design that will allow for potential customers to know what we do as a company and how to reach us.

Information Required:

Phone Number (Placeholder)
Website (PolderClimate.net)

What We Do:

Don't Sweat It.
We're Your 24/7 HVAC Heroes.

Whether you need a temporary temperature solution, or a full-blown HVAC emergency is making you lose your cool – Polder Climate will be there!

We Service:

• Residential
• Office Spaces
• Warehouses
• Retail Locations
• Restaurants
• And Much More!

Target Market(s)

Direct Customers
Contractors

Font styles to use
Sans Serif

Requirements
Must have
• Contact Information
What We Do

```html
<!DOCTYPE html>
<html lang="en">
<head>
<meta charset="utf-8">
<title>Polder Climate – Van Wrap Sides</title>
<link rel="stylesheet" href="https://fonts.googleapis.com/css2?family=Montserrat:wght@400;500;600;700;800&display=swap">
<style>
  :root {
    --page: #ffffff;
    --body-white: #e8e9ea;
    --body-edge: #d3d5d7;
    --wrap-blue: #2b5b8e;
    --wrap-navy: #13314f;
    --ink-blue: #2a4f7e;
    --ink-grey: #4a4d52;
    --ink-light: #e6ecf3;
  }
  html, body {
    margin: 0;
    padding: 0;
    width: 1100px;
    height: 1200px;
    overflow: hidden;
    background: var(--page);
  }
  .canvas {
    width: 1100px;
    height: 1200px;
    display: flex;
    flex-direction: column;
    justify-content: center;
    align-items: center;
    gap: 60px;
  }
  .wrap-side { display: block; }
  .wrap-side text { font-family: "Montserrat", sans-serif; }
  .panel-body { fill: var(--body-white); stroke: var(--body-edge); stroke-width: 2; }
  .wave-band { fill: var(--wrap-blue); }
  .rocker-stripe { fill: var(--wrap-navy); }
  .brand-mark { fill: var(--ink-blue); }
  .brand-name { font-weight: 700; font-size: 38px; fill: var(--ink-blue); letter-spacing: 0.5px; }
  .phone { font-weight: 800; font-size: 52px; fill: var(--ink-blue); }
  .web { font-weight: 400; font-size: 25px; fill: var(--ink-grey); letter-spacing: 0.5px; }
  .tag-lead { font-weight: 400; font-size: 22px; fill: var(--ink-light); letter-spacing: 1px; }
  .tag-bold { font-weight: 800; font-size: 25px; fill: var(--ink-light); letter-spacing: 1px; }
  .service { font-weight: 500; font-size: 20px; fill: var(--ink-light); letter-spacing: 0.5px; }
</style>
</head>
<body>
<main class="canvas">

  <!-- Driver side: cab to the left -->
  <svg class="wrap-side wrap-side--driver" width="1000" height="470" viewBox="0 0 1000 470" aria-label="Driver side wrap panel">
    <rect class="panel-body" x="1" y="1" width="998" height="468" rx="40"/>
    <path class="wave-band" d="M0 350 C 150 320 260 300 360 320 C 470 345 560 320 640 270 C 740 205 850 170 1000 165 L1000 430 Q1000 469 960 469 L40 469 Q0 469 0 430 Z"/>
    <rect class="rocker-stripe" x="280" y="410" width="520" height="34" rx="4"/>

    <rect class="brand-mark" x="374" y="38" width="24" height="24"/>
    <text class="brand-name" x="600" y="64" text-anchor="middle">POLDER CLIMATE</text>
    <text class="phone" x="600" y="132" text-anchor="middle">(555) 014-2790</text>
    <text class="web" x="600" y="168" text-anchor="middle">www.polderclimate.net</text>

    <g transform="rotate(-7 880 230)">
      <text class="tag-lead" x="880" y="222" text-anchor="middle">DON’T SWEAT IT</text>
      <text class="tag-bold" x="880" y="252" text-anchor="middle">WE’RE YOUR</text>
      <text class="tag-bold" x="880" y="278" text-anchor="middle">HVAC HEROES.</text>
    </g>

    <text class="service" x="335" y="345">• RESIDENTIAL</text>
    <text class="service" x="335" y="373">• WAREHOUSES</text>
    <text class="service" x="335" y="401">• RESTAURANTS</text>
    <text class="service" x="545" y="340">• OFFICE SPACES</text>
    <text class="service" x="545" y="368">• RETAIL LOCATIONS</text>
    <text class="service" x="545" y="396">• AND MUCH MORE!</text>
  </svg>

  <!-- Passenger side: cab to the right -->
  <svg class="wrap-side wrap-side--passenger" width="1000" height="470" viewBox="0 0 1000 470" aria-label="Passenger side wrap panel">
    <rect class="panel-body" x="1" y="1" width="998" height="468" rx="40"/>
    <g transform="translate(1000 0) scale(-1 1)">
      <path class="wave-band" d="M0 350 C 150 320 260 300 360 320 C 470 345 560 320 640 270 C 740 205 850 170 1000 165 L1000 430 Q1000 469 960 469 L40 469 Q0 469 0 430 Z"/>
    </g>
    <rect class="rocker-stripe" x="260" y="410" width="520" height="34" rx="4"/>

    <rect class="brand-mark" x="174" y="38" width="24" height="24"/>
    <text class="brand-name" x="400" y="64" text-anchor="middle">POLDER CLIMATE</text>
    <text class="phone" x="400" y="132" text-anchor="middle">(555) 014-2790</text>
    <text class="web" x="400" y="168" text-anchor="middle">www.polderclimate.net</text>

    <g transform="rotate(8 125 230)">
      <text class="tag-lead" x="125" y="222" text-anchor="middle">DON’T SWEAT IT</text>
      <text class="tag-bold" x="125" y="252" text-anchor="middle">WE’RE YOUR</text>
      <text class="tag-bold" x="125" y="278" text-anchor="middle">HVAC HEROES.</text>
    </g>

    <text class="service" x="265" y="345">• RESIDENTIAL</text>
    <text class="service" x="265" y="373">• WAREHOUSES</text>
    <text class="service" x="265" y="401">• RESTAURANTS</text>
    <text class="service" x="480" y="345">• OFFICE SPACES</text>
    <text class="service" x="480" y="373">• RETAIL LOCATIONS</text>
    <text class="service" x="480" y="401">• AND MUCH MORE!</text>
  </svg>

</main>
</body>
</html>
```